Kortiva website design on shopify

Job Description:
As a web designer for Kortiva, you will be the driving force behind designing and developing our new e-commerce website. Your responsibility will be to create an attractive, functional, and intuitive online shopping experience where customers can effortlessly discover and purchase high-quality supplements such as pre-workout, creatine, and protein shakes. Your design will play a crucial role in enhancing our brand and engaging our target audience.

Coding

Coded - Design and coding required

```html
<!DOCTYPE html>
<html lang="en">
<head>
<meta charset="utf-8">
<title>Kortiva — Sports &amp; Health Supplements</title>
<link href="https://fonts.googleapis.com/css2?family=Montserrat:wght@500;600;700&family=Roboto:ital,wght@0,400;0,500;0,700;1,400&display=swap" rel="stylesheet">
<style>
:root{
  --purple:#6a2a8f;
  --purple-dark:#55207a;
  --ink:#151515;
  --muted:#555;
  --line:#d9d9d9;
  --soft:#f3f3f5;
  --footer:#1d1d1f;
  --star:#f2b01e;
  --white:#fff;
}
*{box-sizing:border-box;margin:0;padding:0}
html,body{width:1200px;height:5119px;overflow:hidden}
body{font-family:"Roboto",sans-serif;color:var(--ink);background:var(--white);position:relative}
.abs{position:absolute}
.topbar{top:0;left:0;width:1200px;height:28px;background:var(--purple);color:#fff;font-size:12px;display:flex;align-items:center;justify-content:center}
.nav{top:28px;left:0;width:1200px;height:68px;display:flex;align-items:center;padding:0 100px}
.logo{display:flex;align-items:center;gap:12px;font-family:"Montserrat",sans-serif;font-weight:700;font-size:30px;color:var(--purple);letter-spacing:1px}
.logo-dot{width:34px;height:34px;border-radius:50%;background:var(--purple)}
.nav-links{display:flex;gap:30px;margin-left:auto;font-size:13px;font-weight:500}
.nav-icons{display:flex;gap:14px;margin-left:34px}
.nav-icons svg{width:20px;height:20px;stroke:var(--ink);fill:none;stroke-width:1.8}
.hero{top:96px;left:0;width:1200px;height:627px;background:linear-gradient(100deg,#2a4154 0%,#35526a 40%,#5a6670 65%,#3a3f45 100%)}
.hero-text{top:282px;left:100px;color:#fff;width:380px}
.hero-text h1{font-family:"Montserrat",sans-serif;font-weight:600;font-size:29px;letter-spacing:.5px}
.hero-text p{font-size:15px;line-height:27px;margin-top:14px}
.btn{display:inline-flex;align-items:center;justify-content:center;background:var(--purple);color:#fff;border-radius:16px;font-size:14px}
.hero-text .btn{margin-top:20px;width:130px;height:31px}
.arrow{width:22px;height:40px;stroke-width:1.6;fill:none}
.hero .arrow{stroke:#fff}
.dots{top:693px;left:555px;display:flex;gap:8px}
.dots span{width:22px;height:2px;background:rgba(255,255,255,.5)}
.dots span.on{background:#fff}
.sec-title{left:0;width:1200px;text-align:center}
.sec-title h2{font-family:"Montserrat",sans-serif;font-weight:700;font-size:30px;letter-spacing:.3px}
.sec-title h2 em{font-style:normal;color:var(--purple)}
.sec-title p{font-size:12px;margin-top:6px}
.cat{width:232px;height:231px}
.cat-box{position:absolute;left:0;bottom:0;width:232px;height:151px;background:var(--purple);border-radius:3px;display:flex;align-items:flex-end;justify-content:center;padding-bottom:20px;color:#fff;font-family:"Montserrat",sans-serif;font-weight:500;font-size:16px}
.cat-media{position:absolute;left:51px;top:0;width:130px;height:172px;border-radius:14px;z-index:1}
.tub-dark{background:linear-gradient(180deg,#1c2128,#3b4654 60%,#1a6ea8)}
.tub-red{background:linear-gradient(180deg,#1a1a1a,#c6303a 55%,#1a1a1a)}
.tub-green{background:linear-gradient(180deg,#1c1c1c,#3aa145 55%,#134d1a)}
.tub-white{background:linear-gradient(180deg,#1a1a1a,#f0f0f0 55%,#2a2a2a)}
.tub-gold{background:linear-gradient(180deg,#222,#e7b428 55%,#222)}
.tub-black{background:linear-gradient(180deg,#111,#4a4a4a 55%,#c9d33a)}
.bag-black{background:linear-gradient(180deg,#2a2a2a,#0f0f0f)}
.bag-grey{background:linear-gradient(180deg,#e6e6e6,#bfc2c6)}
.tub-lime{background:linear-gradient(180deg,#1a1a1a,#7fc241 55%,#1a1a1a)}
.tub-purple{background:linear-gradient(180deg,#5b3a9a,#f2d23a 55%,#5b3a9a)}
.tub-organic{background:linear-gradient(180deg,#5aa34a,#eef2e4 55%,#c24a4a)}
.product{width:232px;height:323px;background:#fff;box-shadow:0 2px 10px rgba(0,0,0,.12);text-align:center}
.product-media{width:136px;height:160px;margin:14px auto 0;border-radius:12px}
.product h3{font-family:"Montserrat",sans-serif;font-weight:500;font-size:17px;margin-top:12px}
.stars{color:var(--star);font-size:11px;margin-top:4px;letter-spacing:1px}
.stars span{color:var(--muted);letter-spacing:0;margin-left:4px}
.product .desc{font-size:12px;color:var(--muted);margin-top:6px}
.product .price{font-weight:700;font-size:20px;margin-top:5px}
.product .btn{width:132px;height:30px;margin-top:10px;font-size:14px}
.carousel .arrow{stroke:#333}
.band{top:2176px;left:0;width:1200px;height:437px;background:linear-gradient(115deg,#e8e8ea 0%,#f6f6f7 45%,#ececee 70%,#dcdcdf 100%);overflow:hidden}
.band-copy{top:2296px;left:300px;width:600px;text-align:center}
.band-copy h2{font-family:"Montserrat",sans-serif;font-weight:700;font-size:29px}
.band-copy h2 em{font-style:normal;color:var(--purple)}
.band-copy p{font-size:15px;line-height:27px;margin-top:14px}
.band-copy .btn{margin-top:28px;width:128px;height:31px}
.reviews{top:3175px;left:0;width:1200px;height:441px;background:var(--soft)}
.review{width:320px;height:231px;background:#fff;box-shadow:0 1px 8px rgba(0,0,0,.08);padding:22px 20px}
.review-top{display:flex;justify-content:space-between;font-size:11px;color:var(--muted)}
.review-top .stars{margin:0;font-size:13px}
.review h3{font-size:17px;font-weight:500;margin-top:12px}
.review-body{display:flex;gap:16px;margin-top:14px}
.review-thumb{width:40px;flex:none;font-size:9px;color:var(--muted);text-align:center}
.review-thumb div{width:34px;height:34px;margin:0 auto 6px;border-radius:4px;background:linear-gradient(180deg,#cfd8f0,#6a2a8f)}
.review-body p{font-style:italic;font-size:11px;line-height:20px;color:var(--muted)}
.review .author{font-size:13px;font-weight:700;margin:8px 0 0 56px}
.review .quote{position:absolute;right:16px;bottom:2px;font-family:"Montserrat",sans-serif;font-weight:700;font-size:64px;color:var(--purple);line-height:1}
.brands{top:3752px;left:100px;width:1000px;display:flex;justify-content:space-between;align-items:center}
.brands span{font-family:"Montserrat",sans-serif;font-weight:700;font-size:24px;color:#333}
.rule{top:3864px;height:1px;background:var(--line)}
.view-all{top:3853px;left:0;width:1200px;text-align:center;font-size:16px;color:var(--purple)}
.promo{top:3946px;left:0;width:1200px;height:326px;background:linear-gradient(90deg,#5a2282,#6e2e94,#5a2282);color:#fff;text-align:center}
.promo h2{font-family:"Montserrat",sans-serif;font-weight:700;font-size:24px;line-height:29px;margin-top:76px}
.promo p{font-size:14px;line-height:27px;width:850px;margin:18px auto 0}
.follow{top:4300px;left:0;width:1200px;text-align:center;font-family:"Montserrat",sans-serif;font-weight:700;font-size:30px}
.photo{top:4371px;width:292px;height:330px}
.footer{top:4713px;left:0;width:1200px;height:406px;background:var(--footer);color:#fff}
.fcol{top:4776px}
.fcol h4{font-family:"Montserrat",sans-serif;font-weight:600;font-size:15px;margin-bottom:18px}
.fcol li{list-style:none;font-size:13px;line-height:29px;color:#e6e6e6}
.fcol p{font-size:13px;line-height:29px;color:#e6e6e6}
.contact li{display:flex;align-items:center;gap:8px}
.contact svg{width:12px;height:12px;fill:#fff}
.subscribe{display:flex;margin-top:12px;width:208px;height:34px}
.subscribe span{flex:1;background:#fff;color:#777;font-size:11px;padding:10px}
.subscribe b{width:40px;background:var(--purple);display:flex;align-items:center;justify-content:center}
.socials{display:flex;gap:10px;margin-top:22px}
.socials span{width:42px;height:42px;border:2px solid #fff;border-radius:50%}
.copyright{top:5070px;left:119px;font-size:12px;color:#ddd}
.pay{top:5064px;left:908px;display:flex;gap:4px}
.pay span{width:44px;height:22px;background:#fff;border-radius:3px;color:#333;font-size:8px;font-weight:700;display:flex;align-items:center;justify-content:center}
</style>
</head>
<body>

<div class="abs topbar">→ Free Expedited Shipping on All Orders Over $40 ←</div>

<header class="abs nav">
  <div class="logo"><span class="logo-dot"></span>KORTIVA</div>
  <nav class="nav-links"><span>HOME</span><span>ABOUT US</span><span>ALL PRODUCTS</span><span>SHAKER</span><span>LATEST DEALS</span></nav>
  <div class="nav-icons">
    <svg viewBox="0 0 24 24"><circle cx="10" cy="10" r="7"/><path d="M15 15l6 6"/></svg>
    <svg viewBox="0 0 24 24"><circle cx="12" cy="8" r="4"/><path d="M4 22c0-5 4-8 8-8s8 3 8 8"/></svg>
    <svg viewBox="0 0 24 24"><path d="M12 21s-8-5-8-11a4.5 4.5 0 0 1 8-3 4.5 4.5 0 0 1 8 3c0 6-8 11-8 11z"/></svg>
    <svg viewBox="0 0 24 24"><path d="M5 8h14l-1 13H6z"/><path d="M9 8V6a3 3 0 0 1 6 0v2"/></svg>
  </div>
</header>

<section class="abs hero" role="img" aria-label="Athlete lifting a weight plate beside supplement tubs and a protein bag"></section>
<div class="abs hero-text">
  <h1>WORKOUT ESSENTIALS</h1>
  <p>Lorem ipsum dolor sit amet, tetur adipiscing elit, sed do eiusmod tempor</p>
  <span class="btn">Shop Now</span>
</div>
<svg class="abs arrow hero" style="top:392px;left:64px;stroke:#fff" viewBox="0 0 22 40"><path d="M20 2L2 20l18 18"/></svg>
<svg class="abs arrow" style="top:392px;left:1114px;stroke:#fff" viewBox="0 0 22 40"><path d="M2 2l18 18L2 38"/></svg>
<div class="abs dots"><span></span><span class="on"></span><span></span></div>

<!-- Featured categories -->
<div class="abs sec-title" style="top:792px"><h2>FEATURED <em>CATEGORIES</em></h2><p>The standard Lorem Ipsum passage, used since the sed ut</p></div>
<div class="abs cat" style="top:888px;left:100px"><div class="cat-media tub-dark" role="img" aria-label="Pre-workout tub"></div><div class="cat-box">PRE-WORKOUT</div></div>
<div class="abs cat" style="top:888px;left:356px"><div class="cat-media tub-red" role="img" aria-label="Protein isolate tub"></div><div class="cat-box">PROTEIN SHAKES</div></div>
<div class="abs cat" style="top:888px;left:612px"><div class="cat-media tub-green" role="img" aria-label="Creatine tub"></div><div class="cat-box">CREATINE</div></div>
<div class="abs cat" style="top:888px;left:868px"><div class="cat-media tub-white" role="img" aria-label="Fat burner tub"></div><div class="cat-box">FAT BURNERS</div></div>

<!-- Best sellers -->
<div class="abs sec-title" style="top:1195px"><h2>SHOP THE <em>BEST SELLERS</em></h2><p>The standard Lorem Ipsum passage, used since the sed ut</p></div>
<div class="carousel">
  <svg class="abs arrow" style="top:1420px;left:64px" viewBox="0 0 22 40"><path d="M20 2L2 20l18 18"/></svg>
  <svg class="abs arrow" style="top:1420px;left:1114px" viewBox="0 0 22 40"><path d="M2 2l18 18L2 38"/></svg>
  <div class="abs product" style="top:1288px;left:100px"><div class="product-media tub-gold" role="img" aria-label="Whey protein tub"></div><h3>THE STANDARD</h3><div class="stars">★★★★★<span>(43)</span></div><p class="desc">Sed ut perspiciatis unde omis</p><p class="price">$24.00</p><span class="btn">Add To Cart</span></div>
  <div class="abs product" style="top:1288px;left:356px"><div class="product-media tub-dark" role="img" aria-label="Protein tub"></div><h3>THE STANDARD</h3><div class="stars">★★★★★<span>(43)</span></div><p class="desc">Sed ut perspiciatis unde omis</p><p class="price">$24.00</p><span class="btn">Add To Cart</span></div>
  <div class="abs product" style="top:1288px;left:612px"><div class="product-media tub-black" role="img" aria-label="Protein tub"></div><h3>THE STANDARD</h3><div class="stars">★★★★★<span>(43)</span></div><p class="desc">Sed ut perspiciatis unde omis</p><p class="price">$24.00</p><span class="btn">Add To Cart</span></div>
  <div class="abs product" style="top:1288px;left:868px"><div class="product-media bag-black" role="img" aria-label="Whey protein bag"></div><h3>THE STANDARD</h3><div class="stars">★★★★★<span>(43)</span></div><p class="desc">Sed ut perspiciatis unde omis</p><p class="price">$24.00</p><span class="btn">Add To Cart</span></div>
</div>

<!-- Latest -->
<div class="abs sec-title" style="top:1681px"><h2>SHOP THE <em>LATEST IN STORE</em></h2><p>The standard Lorem Ipsum passage, used since the sed ut</p></div>
<div class="carousel">
  <svg class="abs arrow" style="top:1908px;left:64px" viewBox="0 0 22 40"><path d="M20 2L2 20l18 18"/></svg>
  <svg class="abs arrow" style="top:1908px;left:1114px" viewBox="0 0 22 40"><path d="M2 2l18 18L2 38"/></svg>
  <div class="abs product" style="top:1772px;left:100px"><div class="product-media tub-gold" role="img" aria-label="Whey protein tub"></div><h3>THE STANDARD</h3><div class="stars">★★★★★<span>(43)</span></div><p class="desc">Sed ut perspiciatis unde omis</p><p class="price">$24.00</p><span class="btn">Add To Cart</span></div>
  <div class="abs product" style="top:1772px;left:356px"><div class="product-media bag-grey" role="img" aria-label="Whey protein pouch"></div><h3>THE STANDARD</h3><div class="stars">★★★★★<span>(43)</span></div><p class="desc">Sed ut perspiciatis unde omis</p><p class="price">$24.00</p><span class="btn">Add To Cart</span></div>
  <div class="abs product" style="top:1772px;left:612px"><div class="product-media tub-red" role="img" aria-label="Protein isolate tub"></div><h3>THE STANDARD</h3><div class="stars">★★★★★<span>(43)</span></div><p class="desc">Sed ut perspiciatis unde omis</p><p class="price">$24.00</p><span class="btn">Add To Cart</span></div>
  <div class="abs product" style="top:1772px;left:868px"><div class="product-media tub-lime" role="img" aria-label="Protein blend tub"></div><h3>THE STANDARD</h3><div class="stars">★★★★★<span>(43)</span></div><p class="desc">Sed ut perspiciatis unde omis</p><p class="price">$24.00</p><span class="btn">Add To Cart</span></div>
</div>

<!-- Experience band -->
<section class="abs band">
  <div class="abs tub-lime" style="top:66px;left:22px;width:126px;height:108px;border-radius:20px;transform:rotate(-18deg)" role="img" aria-label="Protein tub tilted"></div>
  <div class="abs tub-white" style="top:278px;left:150px;width:122px;height:159px;border-radius:16px" role="img" aria-label="Fat burner tub"></div>
  <div class="abs bag-black" style="top:200px;left:918px;width:170px;height:232px;border-radius:10px" role="img" aria-label="Whey protein bag"></div>
  <div class="abs tub-red" style="top:-20px;left:1080px;width:150px;height:230px;border-radius:22px;transform:rotate(22deg)" role="img" aria-label="Whey protein tub tilted"></div>
</section>
<div class="abs band-copy">
  <h2>EXPERIENCE <em>THE DIFFERENCE</em></h2>
  <p>Lorem ipsum dolor sit amet, consectetur adipiscing elit, sed do eiusmod tempor incididunt ut labore et dolore magna aa. Quis sum suspendisse ultrices gravida.</p>
  <span class="btn">Shop Now</span>
</div>

<!-- Weekly specials -->
<div class="abs sec-title" style="top:2682px"><h2>WEEKLY <em>SPECIALS</em></h2><p>The standard Lorem Ipsum passage, used since the sed ut</p></div>
<div class="carousel">
  <svg class="abs arrow" style="top:2908px;left:66px" viewBox="0 0 22 40"><path d="M20 2L2 20l18 18"/></svg>
  <svg class="abs arrow" style="top:2908px;left:1114px" viewBox="0 0 22 40"><path d="M2 2l18 18L2 38"/></svg>
  <div class="abs product" style="top:2772px;left:102px"><div class="product-media tub-red" role="img" aria-label="Protein isolate tub"></div><h3>THE STANDARD</h3><div class="stars">★★★★★<span>(43)</span></div><p class="desc">Sed ut perspiciatis unde omis</p><p class="price">$24.00</p><span class="btn">Add To Cart</span></div>
  <div class="abs product" style="top:2772px;left:358px"><div class="product-media tub-gold" role="img" aria-label="Whey protein tub"></div><h3>THE STANDARD</h3><div class="stars">★★★★★<span>(43)</span></div><p class="desc">Sed ut perspiciatis unde omis</p><p class="price">$24.00</p><span class="btn">Add To Cart</span></div>
  <div class="abs product" style="top:2772px;left:614px"><div class="product-media tub-purple" role="img" aria-label="Glossy protein jar"></div><h3>THE STANDARD</h3><div class="stars">★★★★★<span>(43)</span></div><p class="desc">Sed ut perspiciatis unde omis</p><p class="price">$24.00</p><span class="btn">Add To Cart</span></div>
  <div class="abs product" style="top:2772px;left:870px"><div class="product-media tub-organic" role="img" aria-label="Organic protein tub"></div><h3>THE STANDARD</h3><div class="stars">★★★★★<span>(43)</span></div><p class="desc">Sed ut perspiciatis unde omis</p><p class="price">$24.00</p><span class="btn">Add To Cart</span></div>
</div>

<!-- Reviews -->
<section class="abs reviews"></section>
<div class="abs sec-title" style="top:3230px"><h2>CUSTOMER <em>REVIEWS</em></h2><p>The standard Lorem Ipsum passage, used since the sed ut</p></div>
<article class="abs review" style="top:3314px;left:100px">
  <div class="review-top"><div class="stars">★★★★★</div><span>▣ 04-07-2021</span></div>
  <h3>Finibus Bonorum et Malorum sed</h3>
  <div class="review-body"><div class="review-thumb"><div role="img" aria-label="Product thumbnail"></div>Product Name</div><p>Sed ut perspici omnis iste natus error sit vcusantiuque laudantium, totam rem aperiam, eaque ipsa quae ab illo inventore veritatis et quasi</p></div>
  <p class="author">- Daniel Reyes</p><span class="quote">”</span>
</article>
<article class="abs review" style="top:3314px;left:439px">
  <div class="review-top"><div class="stars">★★★★★</div><span>▣ 04-07-2021</span></div>
  <h3>Finibus Bonorum et Malorum sed</h3>
  <div class="review-body"><div class="review-thumb"><div role="img" aria-label="Product thumbnail"></div>Product Name</div><p>Sed ut perspici omnis iste natus error sit vcusantiuque laudantium, totam rem aperiam, eaque ipsa quae ab illo inventore veritatis et quasi</p></div>
  <p class="author">- Daniel Reyes</p><span class="quote">”</span>
</article>
<article class="abs review" style="top:3314px;left:777px">
  <div class="review-top"><div class="stars">★★★★★</div><span>▣ 04-07-2021</span></div>
  <h3>Finibus Bonorum et Malorum sed</h3>
  <div class="review-body"><div class="review-thumb"><div role="img" aria-label="Product thumbnail"></div>Product Name</div><p>Sed ut perspici omnis iste natus error sit vcusantiuque laudantium, totam rem aperiam, eaque ipsa quae ab illo inventore veritatis et quasi</p></div>
  <p class="author">- Daniel Reyes</p><span class="quote">”</span>
</article>

<!-- Brands -->
<div class="abs sec-title" style="top:3678px"><h2>POPULAR <em>BRANDS</em></h2></div>
<div class="abs brands"><span>Ironvale</span><span>Nutrix</span><span>Pulsefit</span><span>Hydrion</span><span>Forgeline</span><span>Stamino</span></div>
<div class="abs rule" style="left:100px;width:400px"></div>
<div class="abs rule" style="left:700px;width:400px"></div>
<div class="abs view-all">View All Brands</div>

<!-- Promo -->
<section class="abs promo">
  <h2>AUSTRALIA'S #1 STORE FOR SPORTS &amp;<br>HEALTH SUPPLEMENTS</h2>
  <p>Lorem ipsum dolor sit amet, consectetur adipiscing elit, sed do eiusmod tempor incididunt ut labore et dolore magna aliqua. Quis ipsum suspendisse ultrices gravida. Risus commodo viverra maecenas accumsan lacus vel facilisis. Lorem ipsum dolor sit amet, consectetur adipiscing elit, sed do eiusmod tempor incididunt ut labore et dolore magna aliqua. Quis ipsum suspendisse ultrices gravida. Risus commodo viverra maecenas accumsan lacus vel facilisis.</p>
</section>

<!-- Follow -->
<div class="abs follow">Follow on @ Kortiva</div>
<div class="abs photo" style="left:0;background:linear-gradient(160deg,#2b5c9e,#4d7fc0 50%,#1d2f55)" role="img" aria-label="Man training on a cable machine in a blue-lit gym"></div>
<div class="abs photo" style="left:302px;background:linear-gradient(160deg,#5c5e62,#8a8a8c 50%,#2f3033)" role="img" aria-label="Man resting on a bench with a shaker bottle"></div>
<div class="abs photo" style="left:604px;background:linear-gradient(160deg,#2a2a2c,#5a5650 50%,#18181a)" role="img" aria-label="Athlete doing a handstand push-up in a dark gym"></div>
<div class="abs photo" style="left:906px;width:294px;background:linear-gradient(160deg,#d7d5cf,#e8d36a 50%,#5a6f8a)" role="img" aria-label="Woman drinking from a shaker bottle after a workout"></div>

<!-- Footer -->
<footer class="abs footer"></footer>
<div class="abs fcol" style="left:119px"><h4>SUPPORT</h4><ul><li>Search</li><li>Become a Seller</li><li>Contact Us</li><li>Refund Policy</li><li>Shipping Policy</li><li>Privacy Policy</li><li>Terms of Service</li></ul></div>
<div class="abs fcol" style="left:310px"><h4>CATEGORIES</h4><ul><li>Pre Workouts</li><li>Fat Burners</li><li>Amino Acids</li><li>Protein Powders</li><li>Nootropics</li></ul></div>
<div class="abs fcol" style="left:499px;width:340px"><h4>PURCHASING &amp;DISTRIBUTION</h4>
  <p>Lorem ipsum dolor sit amet, consectetur ad=lit, sed do eiusmod tempor incididunt ut lablore magna aliqua. Quis ipsum</p>
  <ul class="contact">
    <li><svg viewBox="0 0 12 12"><path d="M0 2h12v8H0z M0 2l6 4 6-4" stroke="#1d1d1f" stroke-width="1"/></svg>info@Kortiva.com</li>
    <li><svg viewBox="0 0 12 12"><path d="M2 0l3 3-1.5 2a7 7 0 0 0 3.5 3.5L9 7l3 3-2 2C5 12 0 7 0 2z"/></svg>1-800-555-0142</li>
    <li><svg viewBox="0 0 12 12"><path d="M6 0a4 4 0 0 1 4 4c0 3-4 8-4 8S2 7 2 4a4 4 0 0 1 4-4z"/></svg>48 Harbor Lane, Suite 3, Brookvale 20931</li>
  </ul>
</div>
<div class="abs fcol" style="left:880px;width:220px"><h4>NEWS &amp; UPDATES</h4>
  <p>Sign up to get the latest on sales, new releases and more ...</p>
  <div class="subscribe"><span>Enter you email</span><b><svg width="16" height="16" viewBox="0 0 16 16"><path d="M1 8l14-7-4 14-3-5z" fill="#fff"/></svg></b></div>
  <div class="socials" aria-label="Social links"><span></span><span></span><span></span><span></span></div>
</div>
<div class="abs copyright">Copyright© 2023 Kortiva . All Rights Reserved.</div>
<div class="abs pay"><span>Paylo</span><span>Cardix</span><span>Amvio</span><span>Banqo</span><span>Finda</span></div>

</body>
</html>
```